KRV e-payment Business Card Design

We require a new business card design to suit our expanding consulting business -who are specialists in 2 main areas
1. Advising large Corporations and Government organisation on how to improve the why they use emerging (B2B) electronic payment systems
2. Educate Global and regional banks on how to design, build and market electronic business payment products in emerging markets

Our logo is grey/silver based with a building block theme. It also suggests "insight" and business know-how capitalizing on our KRV name. We also want to engender trust,security and balance via the ying/yan symbol

The design needs to take into account the target regional areas of Australiasia/Asia Pacific/Middle East and Africa

Target Market(s)

Regional Banks and their business customers

Industry/Entity Type

Electronic

Contact Information for Business Card

Marcus Dellwyn
Director KRV Consulting (Aust) Pty Ltd
PO Box 4736
Brambleton NSW 2164
Australia
tel +61 (0) 2 95316407
mob +61 (0) 438275601
krvconsulting@lumenpost.com

```html
<!DOCTYPE html>
<html lang="en">
<head>
<meta charset="utf-8">
<title>KRV Consulting – Business Card</title>
<link rel="stylesheet" href="https://fonts.googleapis.com/css2?family=Tinos:ital@0;1&display=swap">
<style>
  :root {
    --page-bg: #ffffff;
    --card-dark: #141414;
    --card-mid: #2a2a2a;
    --silver-light: #f2f2f2;
    --silver-mid: #b8b8b8;
    --silver-dark: #6e6e6e;
    --text-main: #f4f4f4;
    --text-muted: #8c8c8c;
    --mark-fill: #c9c9c9;
  }
  * { box-sizing: border-box; margin: 0; padding: 0; }
  html, body {
    width: 1200px; height: 900px; overflow: hidden;
    background: var(--page-bg);
  }
  .business-card {
    position: absolute; left: 100px; top: 144px;
    width: 1000px; height: 612px;
    background: radial-gradient(ellipse at 40% 35%, var(--card-mid), var(--card-dark) 75%);
    font-family: "Tinos", "Times New Roman", serif;
    color: var(--text-main);
  }
  .silver-frame {
    position: absolute; inset: 24px;
    border: 10px solid transparent;
    border-image: linear-gradient(135deg, var(--silver-dark), var(--silver-light) 30%, var(--silver-mid) 55%, var(--silver-light) 80%, var(--silver-dark)) 1;
  }
  .holder {
    position: absolute; right: 60px; top: 62px; text-align: right;
  }
  .holder-name { font-size: 25px; line-height: 30px; letter-spacing: 0.5px; }
  .holder-role { font-size: 22px; line-height: 28px; color: var(--text-muted); }
  .brand-square {
    position: absolute; left: 64px; top: 70px;
    width: 120px; height: 120px; background: var(--mark-fill);
  }
  .brand-name {
    position: absolute; left: 333px; top: 190px;
    font-size: 24px; line-height: 32px; color: var(--text-main);
  }
  .tagline {
    position: absolute; left: 64px; top: 286px;
    font-size: 14px; font-style: italic; color: var(--text-main);
  }
  .contact {
    position: absolute; left: 64px; top: 392px;
    font-size: 24px; line-height: 32px; list-style: none;
  }
</style>
</head>
<body>
  <section class="business-card">
    <div class="silver-frame"></div>

    <div class="holder">
      <p class="holder-name">Marcus Dellwyn</p>
      <p class="holder-role">Director</p>
    </div>

    <span class="brand-square"></span>
    <span class="brand-name">KRV Consulting (Australia) Pty Ltd</span>
    <p class="tagline">“clear e-payment vision”</p>

    <ul class="contact">
      <li>tel&nbsp;&nbsp;&nbsp;: +61 (0) 2 95316407</li>
      <li>mob: +61 (0) 438275601</li>
      <li>krvconsulting@lumenpost.com</li>
      <li>KRV Consulting (Aust) Pty Ltd PO Box 4736</li>
      <li>Brambleton NSW 2164 Australia</li>
    </ul>
  </section>
</body>
</html>
```